High-End audio shop owner needs a business card

I need a personal Business Card for my Audio shop which exists since 1962. We offer high Quality brands, professional Attention and run our own repair-service-department. I look for a design which will be printed on high Quality paper and shall convey trust to the Client that we are very serious. Language is german.

```html
<!DOCTYPE html>
<html lang="de">
<head>
<meta charset="utf-8">
<title>Klanghaus Brenner – Visitenkarte</title>
<link rel="stylesheet" href="https://fonts.googleapis.com/css2?family=Archivo:wght@400;700;800&display=swap">
<style>
  :root {
    --backdrop: #141414;
    --card: #232323;
    --card-edge: #2c2c2c;
    --orange: #f26d21;
    --white: #f4f4f4;
    --grey: #bdbdbd;
  }
  * { margin: 0; padding: 0; box-sizing: border-box; }
  html, body {
    width: 1200px; height: 1200px; overflow: hidden;
    background: var(--backdrop);
    font-family: "Archivo", Arial, sans-serif;
  }
  .canvas {
    position: relative; width: 1200px; height: 1200px;
    display: flex; flex-direction: column; align-items: center; justify-content: center; gap: 60px;
  }
  .card {
    position: relative; width: 880px; height: 503px;
    background: var(--card);
    border: 1px solid var(--card-edge);
    border-radius: 26px;
    overflow: hidden;
  }
  /* back side */
  .card-back .brand {
    position: absolute; left: 0; right: 0; top: 200px;
    text-align: center;
    font-weight: 800; font-size: 50px; letter-spacing: 2px;
    color: var(--white); text-transform: uppercase;
  }
  .card-back .web {
    position: absolute; left: 0; right: 0; bottom: 46px;
    text-align: center; font-weight: 700; font-size: 19px; letter-spacing: 1px;
    color: var(--white);
  }
  .card-back .web .accent { color: var(--orange); }
  /* front side */
  .card-front .brand {
    position: absolute; left: 70px; top: 62px;
    font-weight: 800; font-size: 44px; letter-spacing: 2px;
    color: var(--orange); text-transform: uppercase;
  }
  .person { position: absolute; left: 70px; top: 212px; }
  .person-name {
    font-weight: 700; font-size: 32px; letter-spacing: 1px;
    color: var(--white); text-transform: uppercase;
  }
  .person-role { font-size: 23px; color: var(--orange); margin-top: -2px; }
  .rule-contact {
    position: absolute; left: 60px; top: 302px; width: 470px; height: 2px; background: var(--white);
  }
  .contacts { position: absolute; left: 60px; top: 322px; list-style: none; }
  .contacts li {
    display: flex; align-items: center; gap: 12px;
    font-size: 22px; color: var(--white); line-height: 34px;
  }
  .contacts svg { width: 20px; height: 20px; flex: none; }
  .rule-address {
    position: absolute; left: 540px; top: 376px; width: 290px; height: 2px; background: var(--orange);
  }
  .address {
    position: absolute; right: 50px; top: 392px;
    text-align: right; font-style: normal; font-size: 22px; line-height: 32px; color: var(--white);
  }
</style>
</head>
<body>
<main class="canvas">
  <section class="card card-back" aria-label="Kartenrückseite">
    <div class="brand">Klanghaus Brenner</div>
    <div class="web">www.<span class="accent">klanghaus-brenner</span>.de</div>
  </section>

  <section class="card card-front" aria-label="Kartenvorderseite">
    <div class="brand">Klanghaus Brenner</div>
    <div class="person">
      <div class="person-name">Martin Weber</div>
      <div class="person-role">Managing Partner</div>
    </div>
    <div class="rule-contact"></div>
    <ul class="contacts">
      <li>
        <svg viewBox="0 0 24 24" fill="var(--orange)"><path d="M6.6 10.8a15.1 15.1 0 0 0 6.6 6.6l2.2-2.2a1 1 0 0 1 1-.25 11.4 11.4 0 0 0 3.6.57 1 1 0 0 1 1 1V20a1 1 0 0 1-1 1A17 17 0 0 1 3 4a1 1 0 0 1 1-1h3.5a1 1 0 0 1 1 1c0 1.25.2 2.45.57 3.57a1 1 0 0 1-.25 1z"/></svg>
        089-555-0173
      </li>
      <li>
        <svg viewBox="0 0 24 24" fill="none" stroke="var(--orange)" stroke-width="2"><rect x="2" y="5" width="20" height="14"/><path d="M2 5l10 8 10-8M2 19l7-7M22 19l-7-7"/></svg>
        m.weber@klanghaus-brenner.de
      </li>
      <li>
        <svg viewBox="0 0 24 24" fill="none" stroke="var(--orange)" stroke-width="1.8"><circle cx="12" cy="12" r="10"/><ellipse cx="12" cy="12" rx="4.5" ry="10"/><path d="M2 12h20M4 7h16M4 17h16"/></svg>
        www.klanghaus-brenner.de
      </li>
    </ul>
    <div class="rule-address"></div>
    <address class="address">48 Lindenstraße, Suite 210<br>München, 80331</address>
  </section>
</main>
</body>
</html>
```